Training in Brief Tobacco Use Interventions

We need a design/template for an e-learning course. The course is being created for healthcare professionals. The template should include a home page (title), and subtitle page (introduction, chapter, test, help, references and so on). We would like to see designs that are very professional and appealling.

Reason: Can you extend deadline. I have not heard back from designers.

Target Market(s)

Healthcare professionals

Industry/Entity Type

Health Care

Number of Pages Required

4 page

Font styles to use
Sans Serif

Colors
3276b5
85acd3
ffc214
f37122
ffcf3e
886aae
acd136

Requirements
Must have
• The project's title page should be very professional and appealing for a very serious audience. The title page should include an image of healthcare provider, and/or no smoking symbol.
Nice to have
• Pages should include icons such as next and previous buttons, along with progress status bar on bottom of design. Also should include top row containing for primary chapters. In addition, left side of page should contain space for detailed table of contents and additional resources.
Should not have
• Design should not appear cluttered or confusing. Large space for logo.

```html
<!DOCTYPE html>
<html lang="en">
<head>
<meta charset="utf-8">
<title>Brief Clinical Interventions for Tobacco Use</title>
<link href="https://fonts.googleapis.com/css2?family=Arimo:wght@400;700&family=Open+Sans:wght@400;600&family=Oswald:wght@700&display=swap" rel="stylesheet">
<style>
:root{
  --blue:#3276b5;--blue-soft:#85acd3;--orange:#f37122;--purple:#886aae;--lime:#acd136;
  --green:#2e7d3a;--dark:#222;--darker:#1a1a1a;--ink:#333;--muted:#777;--line:#ddd;--white:#fff;
}
*{box-sizing:border-box;margin:0;padding:0}
html,body{width:742px;height:1200px;overflow:hidden}
body{position:relative;background:var(--white);font-family:"Arimo",Arial,sans-serif;color:var(--ink)}
.abs{position:absolute}
.header{left:0;top:0;width:742px;height:72px;background:var(--white)}
.brand{left:11px;top:33px;height:29px;padding:0 4px;display:flex;align-items:center;gap:6px;font-weight:700;font-size:20px;color:var(--green);white-space:nowrap}
.brand-mark{width:10px;height:10px;background:var(--blue)}
.nav-item{position:absolute;top:53px;font-size:9.5px;line-height:11px;color:#444;text-decoration:none;white-space:nowrap}
.nav-active{position:absolute;left:249px;top:0;width:68px;height:72px;background:var(--orange)}
.nav-item.active{color:var(--white);left:257px}
.hero{left:0;top:72px;width:742px;height:309px;background:var(--blue);overflow:hidden}
.hero-cloud{left:220px;top:30px;width:420px;height:260px;background:radial-gradient(ellipse at center,#3d82c0 0%,var(--blue) 70%)}
.hero-person{left:0;top:22px;width:222px;height:287px;background:linear-gradient(180deg,#e9d9cf 0%,#f4f4f4 60%,#dfe8f0 100%)}
.hero-title{left:234px;top:102px;font-size:22.5px;font-weight:400;color:var(--white);white-space:nowrap}
.hero-rule{left:234px;top:144px;width:200px;height:1px;background:var(--lime)}
.hero-sub{left:436px;top:135px;font-family:"Open Sans",sans-serif;font-size:13.5px;color:var(--lime);white-space:nowrap}
.no-smoke{left:679px;top:183px}
.card{top:401px;width:196px;height:253px;border:1px solid var(--line);border-radius:3px;background:var(--white);overflow:hidden}
.card-head{height:29px;padding:8px 17px;font-size:11.5px;font-weight:700;color:var(--white);white-space:nowrap}
.card-photo{height:127px}
.card-body{padding:17px 17px;font-size:8px;line-height:1.45;color:var(--muted)}
.card-body strong{font-weight:400;color:var(--ink)}
.providers{left:47px;top:689px;width:630px;height:159px;border:1px solid var(--line);border-radius:3px;background:#fafafa;overflow:hidden}
.providers h2{position:absolute;left:17px;top:20px;font-weight:400;font-size:16px;color:var(--blue)}
.providers p{position:absolute;left:20px;width:410px;text-align:center;font-size:8.5px;color:#555;line-height:1.3}
.providers-photo{right:0;top:0;width:199px;height:159px;background:linear-gradient(135deg,#c9b39c 0%,#e8ddd2 50%,#b6c4cf 100%)}
.call{left:0;top:886px;width:742px;height:52px;background:var(--green);font-family:"Oswald",sans-serif;font-weight:700;color:var(--white);font-size:33px;line-height:1}
.call span{position:absolute;top:8px;white-space:nowrap}
.footer{left:0;top:938px;width:742px;height:220px;background:var(--dark);color:#bbb}
.foot-col{top:42px}
.foot-col h3{font-family:"Open Sans",sans-serif;font-weight:400;font-size:12px;color:var(--white);display:flex;align-items:center;gap:7px;padding-bottom:10px;border-bottom:1px solid #444}
.dot{width:9px;height:9px;border:1.5px solid var(--white);border-radius:50%;display:inline-flex;align-items:center;justify-content:center}
.dot::after{content:"";width:3px;height:3px;background:var(--white);border-radius:50%}
.foot-text{font-family:"Open Sans",sans-serif;font-size:7.6px;line-height:1.8;text-align:justify}
.links li{list-style:none;border-bottom:1px solid #3a3a3a;padding:6px 0 7px;font-family:"Open Sans",sans-serif;font-size:7px;color:#777;white-space:nowrap}
.links li b{font-weight:400;font-size:10px;color:var(--white)}
.links li::before{content:"→ ";color:#999}
.vline{top:22px;width:1px;height:178px;background:#3a3a3a}
.social{left:514px;top:170px;display:flex;gap:7px}
.social i{width:22px;height:22px;border-radius:4px;display:block}
.bottom{left:0;top:1158px;width:742px;height:42px;background:var(--darker);color:#aaa;font-family:"Open Sans",sans-serif;font-size:7.5px;text-align:center;line-height:42px}
</style>
</head>
<body>
<header class="header abs">
  <div class="brand abs"><span class="brand-mark"></span>CareCourse</div>
  <nav>
    <div class="nav-active"></div>
    <a class="nav-item active" href="#">Introduction</a>
    <a class="nav-item" href="#" style="left:328px">Tobacco Products</a>
    <a class="nav-item" href="#" style="left:415px">Nicotine Addiction</a>
    <a class="nav-item" href="#" style="left:513px">Brief Interventions</a>
    <a class="nav-item" href="#" style="left:611px">Case Scenarios</a>
    <a class="nav-item" href="#" style="left:688px">Resources</a>
  </nav>
</header>

<section class="hero abs">
  <div class="hero-cloud abs" role="img" aria-label="Faint word cloud of healthcare terms"></div>
  <div class="hero-person abs" role="img" aria-label="Smiling nurse with stethoscope holding a tablet"></div>
  <h1 class="hero-title abs">Brief Clinical Interventions for Tobacco Use</h1>
  <div class="hero-rule abs"></div>
  <p class="hero-sub abs">Tips for Busy Healthcare Providers</p>
</section>
<svg class="no-smoke abs" width="42" height="42" viewBox="0 0 42 42" aria-label="No smoking symbol">
  <circle cx="21" cy="21" r="18" fill="#fff" stroke="#e02020" stroke-width="4"/>
  <rect x="8" y="19" width="20" height="5" fill="#eee" stroke="#999" stroke-width=".6"/>
  <rect x="28" y="19" width="6" height="5" fill="#c8843c"/>
  <line x1="9" y1="33" x2="33" y2="9" stroke="#e02020" stroke-width="4"/>
</svg>

<article class="card abs" style="left:45px">
  <div class="card-head" style="background:var(--orange)">Find a Doctor</div>
  <div class="card-photo" role="img" aria-label="Female doctor in white coat" style="background:linear-gradient(180deg,#e4e4e4,#f6f6f6)"></div>
  <div class="card-body">Search our provider directory to find a doctor, hospital or other health care professional.</div>
</article>
<article class="card abs" style="left:269px;width:194px">
  <div class="card-head" style="background:var(--blue)">Healthcare Online</div>
  <div class="card-photo" role="img" aria-label="Senior doctor with glasses at a computer" style="background:linear-gradient(90deg,#3a3a3a 0%,#bfbfbf 35%,#e5e5e5 100%)"></div>
  <div class="card-body"><strong>A resource for physicians and other health care professionals</strong><br>Find clinical and scientific information from nationally recognized physician experts, advisory boards and professional associations.</div>
</article>
<article class="card abs" style="left:486px">
  <div class="card-head" style="background:var(--purple)">Health Premium<sup style="font-size:6px">®</sup></div>
  <div class="card-photo" role="img" aria-label="Doctor examining a child's ear" style="background:linear-gradient(90deg,#d8cfc8,#ecebe8 60%,#c9c2b8)"></div>
  <div class="card-body"><strong>Recognizing physicians who meet quality and cost efficiency standards<br>Questions about your Veradine Premium designation?</strong> Learn more about the program and see your assessment results.</div>
</article>

<section class="providers abs">
  <h2>Providers</h2>
  <p style="top:68px">We’re working to make the health care experience better—for everyone.</p>
  <p style="top:90px">In an increasingly complex health care environment, Healthcare offers solutions that help health care professionals save time and serve patients.</p>
  <div class="providers-photo abs" role="img" aria-label="Dentist examining a smiling girl's teeth"></div>
</section>

<section class="call abs"><span style="left:57px">Call Us</span><span style="left:468px">+ 00-40404040</span></section>

<footer class="footer abs">
  <div class="foot-col abs" style="left:61px;width:194px">
    <h3><span class="dot"></span>ABOUT US</h3>
    <p class="foot-text" style="margin-top:6px">Lorem Ipsum is simply dummy text of the printing and typesetting industry. Lorem Ipsum has been the industry's standard dummy text ever since the 1500s,Lorem Ipsum is simply dummy text of the printing and typesetting industry. Lorem Ipsum has been the industry's standard dummy text ever since the 1500s,</p>
  </div>
  <div class="vline abs" style="left:276px"></div>
  <div class="foot-col abs" style="left:287px;width:194px">
    <h3 style="border:0;padding-bottom:2px;font-weight:600"><span class="dot"></span>USEFUL LINKS</h3>
    <ul class="links">
      <li>Know more <b>ABOUT US</b></li>
      <li>Explore our <b>WORK</b></li>
      <li>Explore our <b>SERVICES</b></li>
      <li>View client love <b>FOR US</b></li>
      <li style="border:0">Let's talk business <b>CONTACT US</b></li>
    </ul>
  </div>
  <div class="vline abs" style="left:492px"></div>
  <div class="foot-col abs" style="left:505px;width:190px">
    <h3><span class="dot"></span>TESTIMONIAL</h3>
    <svg class="abs" style="left:0;top:40px" width="56" height="44" viewBox="0 0 56 44" aria-hidden="true">
      <ellipse cx="36" cy="14" rx="16" ry="12" fill="#999"/>
      <ellipse cx="20" cy="24" rx="18" ry="14" fill="#555"/>
      <path d="M10 34 L8 42 L18 36Z" fill="#555"/>
      <text x="14" y="30" fill="#fff" font-size="16" font-family="Arial" font-weight="700">“</text>
    </svg>
    <p class="foot-text abs" style="left:65px;top:32px;width:135px">Lorem Ipsum is simply dummy text of the printing and typesetting industry. Lorem Ipsum has been the industry's standard dummy text ever since the 1500s,</p>
  </div>
  <div class="social abs" aria-label="Social links">
    <i style="background:#3b5998"></i><i style="background:#1da1f2"></i><i style="background:#e62117"></i><i style="background:#dd4b39"></i><i style="background:#0e76a8"></i>
  </div>
</footer>
<div class="bottom abs">© Copyright @ 2015 Larkfield Web Studio. All Rights Reserved.</div>
</body>
</html>
```